Life Saving Rules DOKVE

Design a wallet/business card size document front and back to depict the attached lifesaving rules in the color scheme of the business logo attached. (Also attached is an example of a similar card)

Target Market(s)

End User - Field Employees

Industry/Entity Type

Refining

Requirements
Must have
• All Life Saving rules with graphics, using front and back of card, information needs to flow.
Nice to have
• Would like the design to be similar to the card uploaded but better with graphics

```html
<!DOCTYPE html>
<html lang="en">
<head>
<meta charset="utf-8">
<title>Life Saving Rules – DOKVE</title>
<link href="https://fonts.googleapis.com/css2?family=Poppins:wght@300;400;500;600;700&display=swap" rel="stylesheet">
<style>
  :root {
    --page-bg: #dfdfdf;
    --card-bg: #ffffff;
    --band: #0b1f29;
    --blue: #0aa5df;
    --green: #6dbd45;
    --ink: #4a4a4a;
    --ink-strong: #555555;
    --white: #ffffff;
  }
  * { box-sizing: border-box; margin: 0; padding: 0; }
  html, body { width: 1200px; height: 1005px; overflow: hidden; }
  body {
    background: var(--page-bg);
    font-family: "Poppins", sans-serif;
    position: relative;
  }
  .card {
    position: absolute;
    left: 250px;
    width: 700px;
    height: 400px;
    background: var(--card-bg);
    box-shadow: 4px 5px 8px rgba(0,0,0,0.22);
    overflow: hidden;
  }
  .card--front { top: 75px; }
  .card--back { top: 528px; }
  .card__band {
    position: absolute;
    left: 0; top: 0;
    width: 100%;
    height: 150px;
    background: var(--band);
  }
  .card__title {
    position: absolute;
    left: 0; top: 20px;
    width: 100%;
    text-align: center;
    font-size: 56px;
    line-height: 70px;
    font-weight: 700;
    color: var(--white);
    letter-spacing: -0.5px;
  }
  .card__title-accent {
    font-weight: 300;
    color: var(--blue);
    letter-spacing: 0;
  }
  .rule {
    position: absolute;
    top: 103px;
    width: 160px;
    transform: translateX(-50%);
    display: flex;
    flex-direction: column;
    align-items: center;
    text-align: center;
  }
  .rule__badge { width: 132px; height: 92px; display: block; margin-left: 10px; }
  .rule__name {
    margin-top: 6px;
    font-size: 16px;
    line-height: 18px;
    font-weight: 600;
    color: var(--ink-strong);
    white-space: nowrap;
  }
  .rule__divider {
    width: 24px;
    height: 2px;
    background: var(--green);
    margin-top: 7px;
  }
  .rule__text {
    margin-top: 9px;
    font-size: 12px;
    line-height: 14px;
    font-weight: 500;
    color: var(--ink);
  }
  .brand {
    position: absolute;
    left: 0; top: 336px;
    width: 100%;
    display: flex;
    justify-content: center;
    align-items: center;
    gap: 10px;
  }
  .brand__mark {
    width: 14px; height: 14px;
    background: var(--blue);
  }
  .brand__name {
    font-size: 26px;
    line-height: 34px;
    font-weight: 600;
    color: var(--ink-strong);
    letter-spacing: 0.5px;
  }
</style>
</head>
<body>

<svg width="0" height="0" style="position:absolute" aria-hidden="true">
  <defs>
    <g id="diamond">
      <polygon points="69,2 127,46 69,90 11,46" fill="var(--green)"/>
      <polygon points="59,2 117,46 59,90 1,46" fill="var(--blue)"/>
    </g>
  </defs>
</svg>

<!-- Front -->
<section class="card card--front">
  <div class="card__band"></div>
  <h1 class="card__title">Life Saving <span class="card__title-accent">RULES</span></h1>

  <div class="rule" style="left:109px">
    <svg class="rule__badge" viewBox="0 0 132 92" aria-hidden="true">
      <use href="#diamond"/>
      <g fill="none" stroke="var(--white)" stroke-width="2.4" stroke-linecap="round">
        <path d="M47 36 a9 9 0 1 0 10 0"/>
        <line x1="52" y1="31" x2="52" y2="40"/>
      </g>
      <rect x="57" y="46" width="14" height="18" rx="2" fill="var(--white)"/>
      <g stroke="var(--blue)" stroke-width="1.6"><line x1="60" y1="51" x2="68" y2="51"/><line x1="60" y1="55" x2="68" y2="55"/><line x1="60" y1="59" x2="68" y2="59"/></g>
    </svg>
    <h2 class="rule__name">Bypassing Safety<br>Controls</h2>
    <span class="rule__divider"></span>
    <p class="rule__text">Obtain authorization<br>before overriding<br>or disabling<br>safety controls</p>
  </div>

  <div class="rule" style="left:270px">
    <svg class="rule__badge" viewBox="0 0 132 92" aria-hidden="true">
      <use href="#diamond"/>
      <rect x="52" y="30" width="18" height="32" fill="var(--white)"/>
      <rect x="56" y="34" width="4" height="24" fill="var(--blue)"/>
      <line x1="46" y1="32" x2="46" y2="62" stroke="var(--white)" stroke-width="2.4"/>
      <path d="M36 46 l6 0 M39 43 l3 3 -3 3" stroke="var(--white)" stroke-width="2" fill="none" stroke-linecap="round"/>
    </svg>
    <h2 class="rule__name">Confined<br>Space</h2>
    <span class="rule__divider"></span>
    <p class="rule__text">Confined Space<br>Obtain authorization<br>before entering a<br>confined space</p>
  </div>

  <div class="rule" style="left:429px">
    <svg class="rule__badge" viewBox="0 0 132 92" aria-hidden="true">
      <use href="#diamond"/>
      <path d="M52 32 a14 14 0 1 0 10 4" fill="none" stroke="var(--white)" stroke-width="2.4" stroke-linecap="round"/>
      <polygon points="51,36 44,48 50,48 46,58 55,44 49,44 53,36" fill="var(--white)"/>
      <path d="M66 42 v-4 a4 4 0 0 1 8 0 v4" fill="none" stroke="var(--white)" stroke-width="2.2"/>
      <rect x="63" y="42" width="14" height="11" rx="1.5" fill="var(--white)"/>
      <circle cx="70" cy="47" r="1.8" fill="var(--blue)"/>
    </svg>
    <h2 class="rule__name">Energy<br>Isolation</h2>
    <span class="rule__divider"></span>
    <p class="rule__text">Verify isolation<br>and zero<br>energy before<br>work begins</p>
  </div>

  <div class="rule" style="left:587px">
    <svg class="rule__badge" viewBox="0 0 132 92" aria-hidden="true">
      <use href="#diamond"/>
      <path d="M59 30 C62 38 72 42 70 53 C69 59 64 62 59 62 C53 62 48 58 48 52 C48 46 52 43 54 40 C55 45 57 46 59 46 C58 41 57 35 59 30 Z" fill="var(--white)"/>
      <path d="M59 61 C55 61 54 57 56 54 C57 56 59 56 60 53 C62 56 63 58 62 60 Z" fill="var(--blue)"/>
    </svg>
    <h2 class="rule__name">Hot Work</h2>
    <span class="rule__divider"></span>
    <p class="rule__text">Control<br>flammables<br>and ignition<br>sources</p>
  </div>

  <div class="brand">
    <span class="brand__mark"></span>
    <span class="brand__name">DOKVE</span>
  </div>
</section>

<!-- Back -->
<section class="card card--back">
  <div class="card__band"></div>
  <h1 class="card__title">Life Saving <span class="card__title-accent">RULES</span></h1>

  <div class="rule" style="left:159px">
    <svg class="rule__badge" viewBox="0 0 132 92" aria-hidden="true">
      <use href="#diamond"/>
      <g transform="translate(59 46)">
        <circle r="13" fill="none" stroke="var(--white)" stroke-width="6" stroke-dasharray="5 3.2"/>
        <circle r="9" fill="none" stroke="var(--white)" stroke-width="3"/>
        <line x1="-4" y1="4" x2="10" y2="-10" stroke="var(--white)" stroke-width="3.5" stroke-linecap="round"/>
      </g>
    </svg>
    <h2 class="rule__name">Safe Mechanical<br>Lifting</h2>
    <span class="rule__divider"></span>
    <p class="rule__text">Plan lifting<br>operations &amp;<br>control<br>the area</p>
  </div>

  <div class="rule" style="left:347px">
    <svg class="rule__badge" viewBox="0 0 132 92" aria-hidden="true">
      <use href="#diamond"/>
      <rect x="47" y="32" width="24" height="30" rx="2" fill="var(--white)"/>
      <rect x="53" y="29" width="12" height="5" rx="1.5" fill="var(--white)" stroke="var(--blue)" stroke-width="1.2"/>
      <g fill="none" stroke="var(--blue)" stroke-width="1.6" stroke-linecap="round">
        <path d="M50 40 l2 2 3-3"/><line x1="58" y1="40" x2="67" y2="40"/>
        <path d="M50 47 l2 2 3-3"/><line x1="58" y1="47" x2="67" y2="47"/>
        <path d="M50 54 l2 2 3-3"/><line x1="58" y1="54" x2="67" y2="54"/>
      </g>
    </svg>
    <h2 class="rule__name">Work<br>Authorization</h2>
    <span class="rule__divider"></span>
    <p class="rule__text">Work with a<br>valid permit<br>when required</p>
  </div>

  <div class="rule" style="left:533px">
    <svg class="rule__badge" viewBox="0 0 132 92" aria-hidden="true">
      <use href="#diamond"/>
      <rect x="44" y="57" width="16" height="4" fill="var(--white)"/>
      <path d="M62 30 v22 M57 47 l5 5 5-5" fill="none" stroke="var(--white)" stroke-width="3" stroke-linecap="round" stroke-linejoin="round"/>
    </svg>
    <h2 class="rule__name">Fall<br>Protection</h2>
    <span class="rule__divider"></span>
    <p class="rule__text">Protect yourself<br>against fall<br>when working<br>at height</p>
  </div>

  <div class="brand">
    <span class="brand__mark"></span>
    <span class="brand__name">DOKVE</span>
  </div>
</section>

</body>
</html>
```